Brochure Design Project

Need a new look. Customer wants to update 10 year old literature. Very similar "text content" and color scheme only. Need a new modern look. Clean fonts...maybe distressed fonts. Nice salon. Would like brochure to be consistent with their decor...possibly "curvey" graphics maybe simple die-cut if cost effective to produce. Use your imagination! Showed them some pixel harbor work that they liked the look of and I will share these details so you have a feel for the type of work we are looking for.
Updates

Reason: My customer has reviewed the art submissions and though she likes the ideas presented, she has indicated that she needs to stay more consistent with some other collateral which means she would prefer a more mono-chromatic (maybe two or three colors but not a full color glossy brochure. Keeping in mind that she would like a matte look please offer design selections. She has sent me some images of the other collateral she would possibly like to coordinate with which I can send via email upon request.

Target Market(s)

Salon Patrons

Industry/Entity Type

Salon

Requirements
Must have
• Packaged InDesign file upon completion so we can edit down the line(update prices etc.) High Res PDF with marks and bleeds. Must fit into No. 10 envelope(4.125" x 9.5") once folded...I am thinking 9x16 but am open to ideas.
Should not have
• photos...or limit

```html
<!DOCTYPE html>
<html lang="en">
<head>
<meta charset="utf-8">
<title>Lumen Salon Spa – Service Menu Brochure</title>
<link href="https://fonts.googleapis.com/css2?family=Crimson+Text:ital,wght@0,400;1,400&family=PT+Sans:wght@400;700&display=swap" rel="stylesheet">
<style>
  :root{
    --page:#dedede;
    --sheet:#27a9e1;
    --lime:#b6cf2a;
    --ink:#0e1a26;
    --paper:#ffffff;
    --fold:rgba(10,60,90,.35);
  }
  *{box-sizing:border-box;margin:0;padding:0}
  html,body{width:1200px;height:907px;overflow:hidden}
  body{background:var(--page);position:relative;font-family:"PT Sans",Arial,sans-serif;color:var(--ink)}

  .brochure{position:absolute;left:88px;top:217px;width:1023px;height:510px;
    filter:drop-shadow(0 6px 10px rgba(0,0,0,.28))}
  .cover-shape{position:absolute;left:0;top:0;width:252px;height:510px}
  .inner{position:absolute;left:252px;top:0;width:771px;height:510px;background:var(--sheet);display:flex}
  .panel{position:relative;flex:0 0 auto;padding:20px 14px 0 16px;height:100%}
  .panel + .panel{border-left:1px solid var(--fold)}
  .panel-a{width:255px}
  .panel-b{width:256px}
  .panel-c{width:260px}

  .cover{position:absolute;left:0;top:0;width:252px;height:510px}
  .brand{position:absolute;left:48px;top:48px;font-family:"PT Sans",Arial,sans-serif;font-weight:700;
    font-size:20px;line-height:1.05;color:var(--paper);display:flex;align-items:center;gap:7px}
  .brand-dot{width:12px;height:12px;border-radius:50%;background:var(--paper);flex:0 0 auto}
  .intro{position:absolute;left:50px;top:112px;width:188px;font-family:"Crimson Text",Georgia,serif;font-style:italic;
    font-size:8.4px;line-height:1.32;color:var(--paper)}
  .leaf-art{position:absolute;left:64px;top:240px;width:130px;height:246px;border-radius:60px 60px 20px 60px;
    background:radial-gradient(ellipse at 50% 45%,rgba(170,220,245,.75),rgba(120,200,240,.25) 70%,rgba(39,169,225,0) 100%)}
  .crop{position:absolute;height:1px;background:var(--ink);transform-origin:left center}

  .section-title{font-weight:700;font-size:7.6px;letter-spacing:.2px;text-transform:uppercase;
    border-bottom:1px solid var(--ink);padding-bottom:1px;margin:8px 0 3px}
  .section-title:first-child{margin-top:0}
  .service{margin-bottom:3px}
  .service-name{font-weight:700;font-size:7.3px;line-height:1.2}
  .desc{font-family:"Crimson Text",Georgia,serif;font-style:italic;font-size:7.1px;line-height:1.2}
  .price{font-family:"PT Sans",Arial,sans-serif;font-style:normal;font-weight:700;font-size:7px}
  .line{font-size:7px;line-height:1.5}
  .line b{font-weight:700}
  .line i{font-family:"Crimson Text",Georgia,serif}
</style>
</head>
<body>
<div class="brochure">
  <svg class="cover-shape" viewBox="0 0 252 510" aria-hidden="true">
    <path d="M0 0 H252 V510 H70 C40 420 28 330 40 240 C50 160 30 70 0 0 Z" fill="var(--sheet)"/>
    <path d="M0 0 C30 70 50 160 40 240 C28 330 40 420 70 510 H58 C28 420 16 330 28 240 C38 160 18 70 -10 0 Z" fill="var(--lime)"/>
    <path d="M252 250 C236 340 200 420 110 510 H70 C150 430 215 350 252 230 Z" fill="var(--lime)"/>
    <path d="M252 210 C232 320 190 410 96 510" fill="none" stroke="var(--paper)" stroke-width="1.2"/>
  </svg>

  <div class="cover">
    <div class="brand"><span class="brand-dot"></span>Lumen Salon Spa</div>
    <p class="intro">At Lumen salon and spa we are dedicated to making every visit a positive experience. Whether you are here for a day of pampering or for your regular salon appointment, our staff of experienced professionals are dedicated to meeting your every need. Escape the stresses of life and discover a new environment of relaxation and beauty.</p>
    <div class="crop" style="left:82px;top:198px;width:42px;transform:rotate(-38deg)"></div>
    <div class="crop" style="left:170px;top:268px;width:46px;transform:rotate(-40deg)"></div>
    <div class="leaf-art" role="img" aria-label="Pale leafy branch illustration"></div>
  </div>

  <div class="inner">
    <section class="panel panel-a">
      <h2 class="section-title">Massage</h2>
      <div class="service"><div class="service-name">swedish massage</div>
        <p class="desc">Reduces and relieves stress and muscle tension. Induces deep relaxation and improves circulation and range of motion. Target Area (approx. 25 min.) <span class="price">$50</span> | Full Body (approx. 50 min.) <span class="price">$70</span> | Extended Full Body (approx. 80 min.) <span class="price">$120</span></p></div>
      <div class="service"><div class="service-name">prenatal massage</div>
        <p class="desc">Relieves stress on weight bearing joints and reduces deep relaxation. (Always consult your OBGYN) Target Areas <span class="price">$50</span> | Full Body <span class="price">$70</span></p></div>
      <div class="service"><div class="service-name">seated massage</div>
        <p class="desc">The perfect solution for neck and shoulder pain. An abbreviated massage targeted to pressure points of the scalp, neck and shoulders. <span class="price">$25</span></p></div>
      <div class="service"><div class="service-name">four handed massage <span class="desc">(our signature treatment)</span></div>
        <p class="desc">The ultimate relaxation experience. Have two of our skilled therapists work on you simultaneously. target (approx. 30 min.) <span class="price">$100</span> | full body (approx. 60 min.) <span class="price">$140</span></p></div>
      <div class="service"><div class="service-name">hot stone massage</div>
        <p class="desc">This therapeutic treatment incorporates hot stones with classic massage movements. <span class="price">$85</span> (approx. 60 min.)</p></div>
      <div class="service"><div class="service-name">deep tissue massage</div>
        <p class="desc">Goes beyond Swedish Relaxation Massage by going deeper into the tissue or muscles that are responsible for holding chronic pain patterns. <span class="price">$90</span> (approx. 60 min.)</p></div>
      <div class="service"><div class="service-name">scalp massage <span class="desc">(15 min.)</span> <span class="price">$20</span></div></div>
      <div class="service"><div class="service-name">foot massage <span class="desc">(15 min.)</span> <span class="price">$20</span></div></div>

      <h2 class="section-title">Body Treatments</h2>
      <div class="service"><div class="service-name">body scrubs and wraps</div>
        <p class="desc">We offer a full line of customized body scrubs and wraps. These treatments help to exfoliate, remineralize, rehydrate and detoxify. After a consultation with your trained therapist it will be determined which treatment will best suit your needs. Scrubs <span class="price">$50</span> and up | Wraps <span class="price">$50</span> and up | Scrub &amp; Wrap <span class="price">$100</span> and up</p></div>
      <div class="service"><div class="service-name">back treatment</div>
        <p class="desc">This treatment is like a facial for your back. It will help refine the texture and improve the appearance of the skin on the back. This is a must for anyone wearing a backless dress. <span class="price">$55</span></p></div>
      <div class="service"><div class="service-name">sinus treatment</div>
        <p class="desc">This treatment involves steam and localized massage to give you relief from sinus pressure and help encourage the sinuses to drain. <span class="price">$50</span></p></div>

      <h2 class="section-title">Facials</h2>
      <div class="service"><div class="service-name">express facial</div>
        <p class="desc">This facial includes cleansing, steaming, exfoliation, pressure point massage and a 5-minute maintenance treatment mask. <span class="price">$50</span></p></div>
      <div class="service"><div class="service-name">teen facial</div>
        <p class="desc">This is an express facial with a very thorough skin care consultation to address the challenges faced by the teen years. <span class="price">$55</span></p></div>
      <div class="service"><div class="service-name">customized facial</div>
        <p class="desc">This facial is customized to meet any skin care needs you may have. Includes cleansing, steaming, exfoliation on the décolleté, neck and shoulder. Includes a detox massage, pressure point massage and relaxation massage, a 10-15 minute treatment mask, hand, arm, foot and leg massage. Women <span class="price">$70</span> | Men with steam consultation <span class="price">$70</span> | Extractions <span class="price">$10</span></p></div>
    </section>

    <section class="panel panel-b">
      <div class="service"><div class="service-name">natural facial peels</div>
        <p class="desc">Peels are a much deeper form of exfoliation. They go one step beyond a customized facial without the redness and dehydration of some other peeling treatments. These peels are done in conjunction with a Customized Facial. (approx. 90 min.) Royal Peel <span class="price">$110</span> Algae Peel <span class="price">$95</span></p></div>
      <div class="service"><div class="service-name">pumpkin facial</div>
        <p class="desc">Granules and enzymes that encourage the removal of skin cell build up without stress or irritation of the skin. <span class="price">$85</span></p></div>
      <div class="service"><div class="service-name">aura renewal facial</div>
        <p class="desc">Incorporating retinols, glycolics and lactic acids to improve skin tone and texture. <span class="price">$75</span></p></div>
      <div class="service"><div class="service-name">skin brightening facial</div>
        <p class="desc">Helps to improve dull or uneven skin tone, sun and environmentally damaged, mature and hyperpigmented skin. <span class="price">$85</span></p></div>
      <div class="service"><div class="service-name">microdermabrasion</div>
        <p class="desc">Renew and revitalize your skin with this non-invasive exfoliating procedure. This type of skin resurfacing can be performed in an individual session, yet provides optimum results when performed in a series. <span class="price">Call for pricing</span></p></div>
      <div class="service"><div class="service-name">chemical exfoliation / peels</div>
        <p class="desc">Chemical exfoliation can help improve many skin conditions, from acne and hyperpigmentation to dull sun damaged aging skin. Beta Lift, Lactic, Salicylic, Glycolic 30% &amp; 50%, Modified Jessner &amp; TCA <span class="price">$85 – $150</span> (Series pricing available) Must have consultation before booking peel. (15 min.) NO CHARGE</p></div>
      <div class="service"><div class="service-name">hot stone facial</div>
        <p class="desc">Enjoy the benefits of the Customized Facial enhanced by the use of hot and cold stones used during the massage. <span class="price">$85</span></p></div>

      <h2 class="section-title">Body Waxing</h2>
      <div class="service"><div class="service-name">full body waxing</div>
        <p class="desc">(For all waxing services you must have 2-3 weeks growth.)</p></div>
      <p class="line"><b>Lip/Brow/Chin/Sideburns/Stomach $15</b> <i>each area and up</i></p>
      <p class="line"><b>Bikini/Under Arms/Forearms</b> <i>start at</i> <b>$25</b> <i>each service</i></p>
      <p class="line"><b>Full Legs/Men's Back/Men's Chest $50</b> <i>each service</i></p>
      <p class="line"><b>Half Legs/Full Arms $30</b> <i>each service</i></p>
      <p class="line"><b>Brazilian Wax $75</b> <i>and up</i></p>

      <h2 class="section-title">Hair</h2>
      <p class="desc">All services are a la carte.</p>
      <p class="line"><b>Cuts:</b> <i>Women</i> <b>$24</b> <i>and up | Men</i> <b>$21</b> <i>and up | Student</i> <b>$21</b> <i>and up<br>Child (0-11)</i> <b>$15</b> <i>and up | Bang Trim</i> <b>$15</b> <i>and up</i></p>
      <p class="line"><b>Style:</b> <i>Formal</i> <b>$45</b> <i>and up | Brush</i> <b>$35</b> <i>and up | Curled</i> <b>$18</b> <i>and up</i></p>
      <p class="line"><b>Foil:</b> <i>Full</i> <b>$55</b> <i>and up | Half</i> <b>$45</b> <i>and up | Face</i> <b>$35</b> <i>and up</i></p>
      <p class="line"><b>Color:</b> <i>All Over Color</i> <b>$40</b> <i>and up</i></p>
      <p class="line"><b>Perm:</b> <i>Regular $65 and up |</i> <b>Relaxers:</b> <i>Regular</i> <b>$75</b> <i>and up</i></p>

      <h2 class="section-title">Hair Extensions</h2>
      <div class="service"><div class="service-name">human hair extensions</div>
        <p class="desc">We offer natural human hair extensions that last 3-6 months. They attach to small strands of your own hair. Whether you just want to add length, thickness or highlights we have the solution. All our extension specialists have gone through extensive training and are certified by the manufacturer.</p></div>
    </section>

    <section class="panel panel-c">
      <div class="service"><div class="service-name">hair pieces</div>
        <p class="desc">We offer Lumen Hair pieces and Carla Vance clip-in hair pieces that quick and easy total change. They are great for: weddings, prom, special occasions, or everyday. Maybe you are looking to add thickness or a highlighting effect to your own hair we carry human hair and synthetic hairpieces so you can choose.</p></div>
      <div class="service"><div class="service-name">eyelash extensions</div>
        <p class="desc">Eyelash extensions are a revolutionary new way to add length and thickness to your current lashes, they are semi-permanent individual eyelash extensions not your traditional false eyelash strips. They will look and feel like your own lashes. <span class="price">Call for consultation and pricing</span></p></div>

      <h2 class="section-title">Makeup</h2>
      <p class="desc">Includes complimentary mascara</p>
      <p class="line"><b>application: $40 / application with lesson: $70</b></p>
      <p class="line"><b>eyelash and eyebrow tinting: Call for pricing</b></p>

      <h2 class="section-title" style="margin-top:16px">Hands and Feet</h2>
      <div class="service"><div class="service-name">ultimate pedicure</div>
        <p class="desc">Pedicure performed in private spa room. Includes skin mask, hand and arm massage, scalp massage, and foot and leg massage. <span class="price">$75</span> | French <span class="price">$80</span></p></div>
      <div class="service"><div class="service-name">manicure</div>
        <p class="desc">Includes filing and shaping of the nails, trimming cuticles, massage of the hand and polish. <span class="price">$22-$24</span> | French <span class="price">$27</span> and up</p></div>
      <div class="service"><div class="service-name">spa manicure</div>
        <p class="desc">Includes filing and shaping of the nails, trimming cuticles, exfoliation, massage of the hand, hot towel treatment or paraffin treatment and polish. <span class="price">$32-$34</span> | French <span class="price">$37</span> and up</p></div>
      <div class="service"><div class="service-name">pedicure</div>
        <p class="desc">After soaking your feet in the whirlpool, allow us to file and shape the nails, trim the cuticles, rid you of excess dead skin and calluses, massage the feet and polish the nails. <span class="price">$52-$54</span> | French <span class="price">$57</span> and up</p></div>
      <div class="service"><div class="service-name">spa pedicure</div>
        <p class="desc">In addition to everything in the regular pedicure receive an exfoliation and hot towel treatment or paraffin treatment. <span class="price">$62-$64</span> | French <span class="price">$67</span> and up</p></div>
      <div class="service"><div class="service-name">toes to go</div>
        <p class="desc">After soaking your feet in the whirlpool, allow us to file and shape the nails, trim the cuticles and polish the nails. <span class="price">$35</span> | French <span class="price">$40</span> and up</p></div>
      <div class="service"><div class="service-name">polish change</div>
        <p class="desc">Tired of that color but not ready for another manicure just yet... Let us change your polish to improve the look. Fingers <span class="price">$10</span> | Toes <span class="price">$15 + $5</span> for French</p></div>
      <div class="service"><div class="service-name">buff/polish</div>
        <p class="desc">Includes filing and shaping of the nails, buffing and polish. Fingers <span class="price">$15</span> | Toes <span class="price">$20 + $5</span> for French</p></div>
      <div class="service"><div class="service-name">artificial nails</div>
        <p class="desc">Full Set <span class="price">$60</span> and up | Fill-In <span class="price">$30</span> and up | Nail Wrap <span class="price">$50</span><br>Repair <span class="price">$6</span> and up | Soak Off <span class="price">$15</span></p></div>
      <div class="service"><div class="service-name">nail art</div>
        <p class="desc">Consult with a nail technician for specific pricing. <span class="price">$5</span> and up</p></div>
    </section>
  </div>
</div>
</body>
</html>
```